Design for web app with Brindle Surface System - Tarvo7 SMS consult

We are developing a web app that will work in browsers. Its main purpose is to allow for users (signing up and logging in with their phone number) to track their habbits and select consultants to whom they can send SMS for help.

The wireframes of the app can be accessed here (pdf):
https://files.quellbox.example/d/7Kx2PmR9vTq4LnZ8wYs3HbJ6cFe1/view?usp=sharing

NB!: Please do not follow the mockups 100% literally, but the Brindle Surface system guidelines.

The technical specifications and descriptions of the web app's functionalities are available in the link below:
https://pages.quellbox.example/document/d/4TrNk8WqZp2LmVx7YcBs9HdJ3fRe6GaU1oKi5QeXtwy0/edit?usp=sharing

Requirements for the design:

- The design should be provided as PSD, where each page/section should be in its own PSD file OR all pages/sections should be represented as folder groups in a single PSD file.

- All graphical elements in the design should be delivered as single layers which can then be extracted from the PSD.

- All graphical elements (icons, graphical buttons, etc.) should be provided as vector objects in the PSD, so that they can be exported into different sizes without loss of quality (for responsiveness).

- The design should use either web safe fonts or Brindle Type.

Instructions for the design:
The design should be based on Brindle Surface System - http://www.brindle.example/design/spec/surface-system/introduction.html

Please also provide an app icon and suggest a logo for the app.

• Based on Brindle Surface System
• Flat
• Nice looking and not so stiff as the default Brindle Surface System, but it is important to follow their guidelines.
• 3D

```html
<!DOCTYPE html>
<html lang="en">
<head>
<meta charset="utf-8">
<title>Tarvo7 SMS consult – app screens</title>
<link rel="stylesheet" href="https://fonts.googleapis.com/css2?family=Open+Sans:wght@300;400;600&display=swap">
<style>
:root{
  --canvas:#22252c;
  --rule:#4a4e57;
  --slate:#3f4451;
  --slate-off:#393d47;
  --bar:#3d424d;
  --surface:#f2f2f2;
  --row:#ffffff;
  --row-alt:#ececec;
  --rail:#d9d9d9;
  --blue:#0e6fae;
  --cyan:#27b3ea;
  --yellow:#fcc54c;
  --yellow-ink:#5b4a1f;
  --green:#2fbf8d;
  --red:#f15b3e;
  --ink:#4a4a4a;
  --muted:#9a9a9a;
  --pale:#e4e4e4;
  --photo:linear-gradient(160deg,#d2ab86,#6d4b37);
}
*{box-sizing:border-box}
html,body{margin:0;width:989px;height:1200px;overflow:hidden;background:var(--canvas)}
.defs{position:absolute;width:0;height:0}
.divider{position:absolute;left:496px;top:0;width:1px;height:1200px;background:var(--rule)}

.screen{position:absolute;width:115px;height:204px;background:var(--surface);overflow:hidden;font-family:'Open Sans',sans-serif;color:var(--ink)}
.screen>*{position:absolute}
.screen.dark{background:var(--slate)}
.screen.off{background:var(--slate-off)}
.c1{left:34px}.c2{left:186px}.c3{left:338px}.c4{left:534px}.c5{left:686px}.c6{left:839px}
.r1{top:56px}.r2{top:344px}.r3{top:632px}.r4{top:920px}

/* splash */
.brand{left:14px;top:90px;display:flex;align-items:center;gap:3px}
.brand-mark{width:7px;height:7px;background:var(--blue)}
.brand-name{font-size:9px;font-weight:600;color:#fff}
.splash-note{left:0;top:174px;width:115px;text-align:center;font-size:2.8px;line-height:4px;color:#8a8f9a}

/* auth */
.auth-title{left:0;width:115px;text-align:center;color:#fff;font-size:7px;font-weight:300;letter-spacing:.3px}
.field{left:14px;width:87px;height:12px;background:#fff;display:flex;align-items:center;padding-left:4px}
.field svg{width:5px;height:5px;fill:#aaa}
.auth-btn{left:14px;width:87px;height:11px}
.forgot{left:0;width:115px;text-align:center;font-size:3px;color:#c8cbd2}

/* shared */
.btn{height:13px;display:flex;align-items:center;justify-content:center;gap:2px;font-size:4px;color:#fff}
.btn.blue{background:var(--blue)}
.btn.yellow{background:var(--yellow);color:var(--yellow-ink)}
.btn.full{left:4px;width:107px;top:180px}
.btn.half-l{left:4px;width:45px;top:180px}
.btn.half-r{left:62px;width:45px;top:180px}
.btn svg{width:4px;height:4px;fill:#fff}
.appbar{left:0;top:0;width:115px;height:26px;background:var(--bar);color:#fff;font-size:5px;display:flex;align-items:center;gap:10px;padding-left:7px}
.appbar svg{width:7px;height:7px;fill:#fff}
.select{left:4px;top:30px;width:107px;height:10px;background:#fff;font-size:3.5px;color:var(--muted);display:flex;align-items:center;justify-content:space-between;padding:0 4px}
.select svg{width:4px;height:4px;fill:var(--muted)}
.label{left:4px;font-size:3.5px;color:var(--muted)}

/* consultant list */
.list{left:0;top:26px;width:115px;margin:0;padding:0;list-style:none}
.list li{position:relative;height:19px;display:flex;align-items:center;gap:5px;padding-left:5px;font-size:4.5px;background:var(--row)}
.list li:nth-child(even){background:var(--row-alt)}
.avatar{width:8px;height:8px;border-radius:50%;background:var(--photo)}
.rail{position:absolute;right:0;top:0;width:18px;height:19px;background:var(--rail);display:flex;align-items:center;justify-content:center}
.rail.on{background:var(--yellow)}
.rail svg{width:8px;height:8px;fill:#fff}
.rail.photo{background:var(--photo)}
.rail.photo.on{box-shadow:inset 3px 0 0 var(--yellow)}

/* contact notes */
.datebar{left:0;top:26px;width:115px;height:12px;background:var(--cyan);color:#fff;font-size:4px;display:flex;align-items:center;justify-content:space-between;padding:0 6px}
.datebar svg{width:5px;height:5px;fill:#fff}
.actions{left:0;top:38px;width:115px;height:20px;display:grid;grid-template-columns:repeat(3,1fr)}
.actions span{display:flex;flex-direction:column;align-items:center;justify-content:center;gap:1px;color:#fff;font-size:2.6px}
.actions svg{width:8px;height:8px;fill:#fff}
.act-call{background:var(--cyan)}.act-good{background:var(--green)}.act-bad{background:var(--red)}
.topic{left:4px;top:62px;width:107px;height:9px;background:#fff;font-size:3.2px;color:var(--muted);display:flex;align-items:center;padding-left:3px}
.notes-area{left:4px;top:82px;width:107px;height:84px;background:#fff}

/* week grid */
.week{left:4px;width:107px;display:grid;grid-template-columns:repeat(3,1fr)}
.tile{display:flex;flex-direction:column;align-items:center;justify-content:center;gap:2px;color:#fff;font-size:3px;border:.5px solid rgba(255,255,255,.55)}
.tile svg{width:9px;height:9px;fill:#fff}
.tile.good{background:var(--green)}
.tile.bad{background:var(--red)}
.tile.none{background:var(--pale)}
.week.tall .tile{height:31px}
.week.short .tile{height:18px}
.week.short .tile svg{width:7px;height:7px}

/* month */
.cal{left:4px;top:44px;width:107px;display:grid;grid-template-columns:repeat(7,1fr);row-gap:4px;font-size:3.6px;text-align:center}
.cal span{padding-bottom:2px;border-bottom:2px solid transparent}
.cal .g{border-color:var(--green)}
.cal .r{border-color:var(--red)}
.cal .head{color:var(--muted)}

/* message */
.hint{left:0;top:26px;width:115px;height:11px;background:var(--cyan);color:#fff;font-size:2.8px;line-height:3.6px;padding:1px 4px}
.message-area{left:4px;top:40px;width:107px;height:132px;background:#fff}

/* confirmation */
.sent-avatar{left:43px;top:50px;width:29px;height:29px;border-radius:50%;border:2px solid #fff;background:var(--photo)}
.sent-text{left:0;top:88px;width:115px;text-align:center;font-size:4.3px;line-height:5.5px;color:#fff}
.sent-ok{left:43px;top:110px;width:29px;height:10px}
</style>
</head>
<body>
<svg class="defs" aria-hidden="true">
  <symbol id="i-back" viewBox="0 0 16 16"><path d="M15 7H4.8l4.6-4.6L8 1 1 8l7 7 1.4-1.4L4.8 9H15z"/></symbol>
  <symbol id="i-up" viewBox="0 0 16 16"><path d="M1 7h3v8H1zM5 7l3.5-6c1.3 0 2.2 1 1.8 2.6L9.6 6H14c1 0 1.7.9 1.4 1.9l-1.8 5.8c-.2.8-.9 1.3-1.7 1.3H5z"/></symbol>
  <symbol id="i-down" viewBox="0 0 16 16"><g transform="rotate(180 8 8)"><path d="M1 7h3v8H1zM5 7l3.5-6c1.3 0 2.2 1 1.8 2.6L9.6 6H14c1 0 1.7.9 1.4 1.9l-1.8 5.8c-.2.8-.9 1.3-1.7 1.3H5z"/></g></symbol>
  <symbol id="i-phone" viewBox="0 0 16 16"><path d="M4 1l2.5 3.5-1.6 1.8a9 9 0 0 0 4.8 4.8l1.8-1.6L15 12l-1.5 2.6C7 15 1 9 1.4 2.5z"/></symbol>
  <symbol id="i-lock" viewBox="0 0 16 16"><path d="M4 7V5a4 4 0 0 1 8 0v2h1v8H3V7zm2 0h4V5a2 2 0 0 0-4 0z"/></symbol>
  <symbol id="i-tick" viewBox="0 0 16 16"><path d="M6 11.2 2.8 8 1.4 9.4 6 14 15 5l-1.4-1.4z"/></symbol>
  <symbol id="i-chat" viewBox="0 0 16 16"><path d="M1 2h14v9H6l-4 3v-3H1z"/></symbol>
  <symbol id="i-left" viewBox="0 0 16 16"><path d="M11 1 4 8l7 7 1.4-1.4L6.8 8l5.6-5.6z"/></symbol>
  <symbol id="i-right" viewBox="0 0 16 16"><path d="M5 1 3.6 2.4 9.2 8l-5.6 5.6L5 15l7-7z"/></symbol>
  <symbol id="i-caret" viewBox="0 0 16 16"><path d="M3 5h10l-5 6z"/></symbol>
  <symbol id="i-stats" viewBox="0 0 16 16"><path d="M1 15h14v-1H1zM2 9h3v4H2zm4.5-5h3v9h-3zM11 6h3v7h-3z"/></symbol>
</svg>

<div class="divider"></div>

<!-- ===== left set ===== -->
<section class="screen dark c1 r1">
  <div class="brand"><span class="brand-mark"></span><span class="brand-name">Tarvo7</span></div>
  <p class="splash-note" style="margin:0">Track habits with care<br>Version 1.0 built for daily progress</p>
</section>

<section class="screen dark c2 r1">
  <h1 class="auth-title" style="top:46px;margin:0">SIGN IN</h1>
  <div class="field" style="top:60px"><svg><use href="#i-phone"/></svg></div>
  <div class="field" style="top:77px"><svg><use href="#i-lock"/></svg></div>
  <div class="btn blue auth-btn" style="top:95px">LOGIN</div>
  <div class="btn yellow auth-btn" style="top:114px">REGISTER</div>
  <p class="forgot" style="top:132px;margin:0">FORGOT YOUR PASSWORD?</p>
</section>

<section class="screen dark c3 r1">
  <h1 class="auth-title" style="top:62px;margin:0">REGISTER</h1>
  <div class="field" style="top:76px"><svg><use href="#i-phone"/></svg></div>
  <div class="btn blue auth-btn" style="top:95px">LOGIN</div>
  <div class="btn yellow auth-btn" style="top:112px">CANCEL</div>
</section>

<section class="screen c1 r2">
  <header class="appbar"><svg><use href="#i-back"/></svg>Select your consultant's</header>
  <ul class="list">
    <li><span class="avatar" role="img" aria-label="Consultant portrait"></span>Lorem Ipsum<span class="rail on"><svg><use href="#i-tick"/></svg></span></li>
    <li><span class="avatar" role="img" aria-label="Consultant portrait"></span>Dolor sit amet<span class="rail"></span></li>
    <li><span class="avatar" role="img" aria-label="Consultant portrait"></span>Consectetuer<span class="rail"></span></li>
    <li><span class="avatar" role="img" aria-label="Consultant portrait"></span>Adipiscing<span class="rail on"><svg><use href="#i-tick"/></svg></span></li>
    <li><span class="avatar" role="img" aria-label="Consultant portrait"></span>Nonummy<span class="rail"></span></li>
    <li><span class="avatar" role="img" aria-label="Consultant portrait"></span>Euismod<span class="rail"></span></li>
    <li><span class="avatar" role="img" aria-label="Consultant portrait"></span>Tincidunt<span class="rail"></span></li>
  </ul>
  <div class="btn blue full">Continue</div>
</section>

<section class="screen c2 r2">
  <header class="appbar"><svg><use href="#i-back"/></svg>Contact Notes</header>
  <div class="datebar"><svg><use href="#i-left"/></svg>02.04.2015<svg><use href="#i-right"/></svg></div>
  <div class="actions"><span class="act-call"><svg><use href="#i-phone"/></svg>Call Me</span><span class="act-good"><svg><use href="#i-up"/></svg></span><span class="act-bad"><svg><use href="#i-down"/></svg></span></div>
  <div class="topic">I wish to discuss my health situation</div>
  <span class="label" style="top:74px">Notes :</span>
  <div class="notes-area"></div>
  <div class="btn blue half-l"><svg><use href="#i-stats"/></svg>Statistic</div>
  <div class="btn yellow half-r">Save</div>
</section>

<section class="screen c3 r2">
  <header class="appbar"><svg><use href="#i-back"/></svg>Week Reviews</header>
  <div class="select">Last Week<svg><use href="#i-caret"/></svg></div>
  <span class="label" style="top:43px">Week 14</span>
  <div class="week tall" style="top:50px">
    <div class="tile good"><svg><use href="#i-up"/></svg>Monday</div>
    <div class="tile bad"><svg><use href="#i-down"/></svg>Tuesday</div>
    <div class="tile good"><svg><use href="#i-up"/></svg>Wednesday</div>
    <div class="tile bad"><svg><use href="#i-down"/></svg>Thursday</div>
    <div class="tile good"><svg><use href="#i-up"/></svg>Friday</div>
    <div class="tile good"><svg><use href="#i-up"/></svg>Saturday</div>
    <div class="tile good"><svg><use href="#i-up"/></svg>Sunday</div>
    <div class="tile none"></div>
    <div class="tile none"></div>
  </div>
  <div class="btn yellow full">Back</div>
</section>

<section class="screen c1 r3">
  <header class="appbar"><svg><use href="#i-back"/></svg>Week Reviews</header>
  <div class="select">Last Two Weeks<svg><use href="#i-caret"/></svg></div>
  <span class="label" style="top:43px">Week 13</span>
  <div class="week short" style="top:50px">
    <div class="tile bad"><svg><use href="#i-down"/></svg></div>
    <div class="tile good"><svg><use href="#i-up"/></svg></div>
    <div class="tile good"><svg><use href="#i-up"/></svg></div>
    <div class="tile good"><svg><use href="#i-up"/></svg></div>
    <div class="tile good"><svg><use href="#i-up"/></svg></div>
    <div class="tile good"><svg><use href="#i-up"/></svg></div>
    <div class="tile bad"><svg><use href="#i-down"/></svg></div>
    <div class="tile none"></div>
    <div class="tile none"></div>
  </div>
  <span class="label" style="top:106px">Week 14</span>
  <div class="week short" style="top:113px">
    <div class="tile good"><svg><use href="#i-up"/></svg></div>
    <div class="tile bad"><svg><use href="#i-down"/></svg></div>
    <div class="tile good"><svg><use href="#i-up"/></svg></div>
    <div class="tile good"><svg><use href="#i-up"/></svg></div>
    <div class="tile bad"><svg><use href="#i-down"/></svg></div>
    <div class="tile good"><svg><use href="#i-up"/></svg></div>
    <div class="tile good"><svg><use href="#i-up"/></svg></div>
    <div class="tile none"></div>
    <div class="tile none"></div>
  </div>
  <div class="btn yellow full">Back</div>
</section>

<section class="screen c2 r3">
  <header class="appbar"><svg><use href="#i-back"/></svg>Month Reviews</header>
  <div class="select">Last Month<svg><use href="#i-caret"/></svg></div>
  <div class="cal">
    <span class="head">M</span><span class="head">T</span><span class="head">W</span><span class="head">T</span><span class="head">F</span><span class="head">S</span><span class="head">S</span>
    <span></span><span></span><span class="g">1</span><span class="g">2</span><span class="r">3</span><span class="g">4</span><span class="g">5</span>
    <span class="g">6</span><span class="g">7</span><span class="g">8</span><span class="g">9</span><span class="g">10</span><span class="g">11</span><span class="g">12</span>
    <span class="g">13</span><span class="r">14</span><span class="g">15</span><span class="g">16</span><span class="g">17</span><span class="r">18</span><span class="g">19</span>
    <span class="g">20</span><span class="g">21</span><span class="r">22</span><span class="g">23</span><span class="g">24</span><span class="g">25</span><span class="g">26</span>
    <span class="g">27</span><span class="g">28</span><span class="g">29</span><span class="g">30</span><span class="g">31</span><span></span><span></span>
  </div>
  <div class="btn yellow full">Back</div>
</section>

<section class="screen c3 r3">
  <header class="appbar"><svg><use href="#i-back"/></svg>Send SMS to Consultan's</header>
  <ul class="list">
    <li><span class="avatar" role="img" aria-label="Consultant portrait"></span>Lorem Ipsum<span class="rail on"><svg><use href="#i-chat"/></svg></span></li>
    <li><span class="avatar" role="img" aria-label="Consultant portrait"></span>Dolor sit amet<span class="rail"></span></li>
    <li><span class="avatar" role="img" aria-label="Consultant portrait"></span>Consectetuer<span class="rail"></span></li>
    <li><span class="avatar" role="img" aria-label="Consultant portrait"></span>Adipiscing<span class="rail"></span></li>
    <li><span class="avatar" role="img" aria-label="Consultant portrait"></span>Nonummy<span class="rail"></span></li>
    <li><span class="avatar" role="img" aria-label="Consultant portrait"></span>Euismod<span class="rail"></span></li>
    <li><span class="avatar" role="img" aria-label="Consultant portrait"></span>Tincidunt<span class="rail"></span></li>
  </ul>
  <div class="btn yellow full">Back</div>
</section>

<section class="screen c1 r4">
  <header class="appbar"><svg><use href="#i-back"/></svg>Send Message</header>
  <p class="hint" style="margin:0">Please write the text for the SMS and confirm that you want to send it.</p>
  <div class="message-area"></div>
  <div class="btn yellow half-l">Cancel</div>
  <div class="btn blue half-r">Send</div>
</section>

<section class="screen dark c2 r4">
  <div class="sent-avatar" role="img" aria-label="Portrait of the selected consultant"></div>
  <p class="sent-text" style="margin:0">Lorem Ipsum has now<br>received your SMS</p>
  <div class="btn yellow sent-ok">OK</div>
</section>

<section class="screen off c3 r4"></section>

<!-- ===== right set ===== -->
<section class="screen dark c4 r1">
  <div class="brand"><span class="brand-mark"></span><span class="brand-name">Tarvo7</span></div>
  <p class="splash-note" style="margin:0">Track habits with care<br>Version 1.0 built for daily progress</p>
</section>

<section class="screen dark c5 r1">
  <h1 class="auth-title" style="top:46px;margin:0">SIGN IN</h1>
  <div class="field" style="top:60px"><svg><use href="#i-phone"/></svg></div>
  <div class="field" style="top:77px"><svg><use href="#i-lock"/></svg></div>
  <div class="btn blue auth-btn" style="top:95px">LOGIN</div>
  <div class="btn yellow auth-btn" style="top:114px">REGISTER</div>
  <p class="forgot" style="top:132px;margin:0">FORGOT YOUR PASSWORD?</p>
</section>

<section class="screen dark c6 r1">
  <h1 class="auth-title" style="top:62px;margin:0">REGISTER</h1>
  <div class="field" style="top:76px"><svg><use href="#i-phone"/></svg></div>
  <div class="btn blue auth-btn" style="top:95px">LOGIN</div>
  <div class="btn yellow auth-btn" style="top:112px">CANCEL</div>
</section>

<section class="screen c4 r2">
  <header class="appbar"><svg><use href="#i-back"/></svg>Select your consultant's</header>
  <ul class="list">
    <li>Lorem Ipsum<span class="rail photo on" role="img" aria-label="Consultant portrait, selected"></span></li>
    <li>Dolor sit amet<span class="rail photo" role="img" aria-label="Consultant portrait"></span></li>
    <li>Consectetuer<span class="rail photo" role="img" aria-label="Consultant portrait"></span></li>
    <li>Adipiscing<span class="rail photo on" role="img" aria-label="Consultant portrait, selected"></span></li>
    <li>Nonummy<span class="rail photo" role="img" aria-label="Consultant portrait"></span></li>
    <li>Euismod<span class="rail photo" role="img" aria-label="Consultant portrait"></span></li>
    <li>Tincidunt<span class="rail photo" role="img" aria-label="Consultant portrait"></span></li>
  </ul>
  <div class="btn blue full">Continue</div>
</section>

<section class="screen c5 r2">
  <header class="appbar"><svg><use href="#i-back"/></svg>Contact Notes</header>
  <div class="datebar"><svg><use href="#i-left"/></svg>02.04.2015<svg><use href="#i-right"/></svg></div>
  <div class="actions"><span class="act-call"><svg><use href="#i-phone"/></svg>Call Me</span><span class="act-good"><svg><use href="#i-up"/></svg></span><span class="act-bad"><svg><use href="#i-down"/></svg></span></div>
  <div class="topic">I wish to discuss my health situation</div>
  <span class="label" style="top:74px">Notes :</span>
  <div class="notes-area"></div>
  <div class="btn blue half-l"><svg><use href="#i-stats"/></svg>Statistic</div>
  <div class="btn yellow half-r">Save</div>
</section>

<section class="screen c6 r2">
  <header class="appbar"><svg><use href="#i-back"/></svg>Week Reviews</header>
  <div class="select">Last Week<svg><use href="#i-caret"/></svg></div>
  <span class="label" style="top:43px">Week 14</span>
  <div class="week tall" style="top:50px">
    <div class="tile good"><svg><use href="#i-up"/></svg>Monday</div>
    <div class="tile bad"><svg><use href="#i-down"/></svg>Tuesday</div>
    <div class="tile good"><svg><use href="#i-up"/></svg>Wednesday</div>
    <div class="tile bad"><svg><use href="#i-down"/></svg>Thursday</div>
    <div class="tile good"><svg><use href="#i-up"/></svg>Friday</div>
    <div class="tile good"><svg><use href="#i-up"/></svg>Saturday</div>
    <div class="tile good"><svg><use href="#i-up"/></svg>Sunday</div>
    <div class="tile none"></div>
    <div class="tile none"></div>
  </div>
  <div class="btn yellow full">Back</div>
</section>

<section class="screen c4 r3">
  <header class="appbar"><svg><use href="#i-back"/></svg>Week Reviews</header>
  <div class="select">Last Two Weeks<svg><use href="#i-caret"/></svg></div>
  <span class="label" style="top:43px">Week 13</span>
  <div class="week short" style="top:50px">
    <div class="tile bad"><svg><use href="#i-down"/></svg></div>
    <div class="tile good"><svg><use href="#i-up"/></svg></div>
    <div class="tile good"><svg><use href="#i-up"/></svg></div>
    <div class="tile good"><svg><use href="#i-up"/></svg></div>
    <div class="tile good"><svg><use href="#i-up"/></svg></div>
    <div class="tile good"><svg><use href="#i-up"/></svg></div>
    <div class="tile bad"><svg><use href="#i-down"/></svg></div>
    <div class="tile none"></div>
    <div class="tile none"></div>
  </div>
  <span class="label" style="top:106px">Week 14</span>
  <div class="week short" style="top:113px">
    <div class="tile good"><svg><use href="#i-up"/></svg></div>
    <div class="tile bad"><svg><use href="#i-down"/></svg></div>
    <div class="tile good"><svg><use href="#i-up"/></svg></div>
    <div class="tile good"><svg><use href="#i-up"/></svg></div>
    <div class="tile bad"><svg><use href="#i-down"/></svg></div>
    <div class="tile good"><svg><use href="#i-up"/></svg></div>
    <div class="tile good"><svg><use href="#i-up"/></svg></div>
    <div class="tile none"></div>
    <div class="tile none"></div>
  </div>
  <div class="btn yellow full">Back</div>
</section>

<section class="screen c5 r3">
  <header class="appbar"><svg><use href="#i-back"/></svg>Month Reviews</header>
  <div class="select">Last Month<svg><use href="#i-caret"/></svg></div>
  <div class="cal">
    <span class="head">M</span><span class="head">T</span><span class="head">W</span><span class="head">T</span><span class="head">F</span><span class="head">S</span><span class="head">S</span>
    <span></span><span></span><span class="g">1</span><span class="g">2</span><span class="g">3</span><span class="r">4</span><span class="g">5</span>
    <span class="g">6</span><span class="g">7</span><span class="g">8</span><span class="g">9</span><span class="g">10</span><span class="g">11</span><span class="g">12</span>
    <span class="g">13</span><span class="r">14</span><span class="g">15</span><span class="g">16</span><span class="g">17</span><span class="g">18</span><span class="r">19</span>
    <span class="g">20</span><span class="g">21</span><span class="r">22</span><span class="g">23</span><span class="g">24</span><span class="g">25</span><span class="g">26</span>
    <span class="g">27</span><span class="g">28</span><span class="g">29</span><span class="g">30</span><span></span><span></span><span></span>
  </div>
  <div class="btn yellow full">Back</div>
</section>

<section class="screen c6 r3">
  <header class="appbar"><svg><use href="#i-back"/></svg>Send SMS to Consultan's</header>
  <ul class="list">
    <li>Lorem Ipsum<span class="rail photo on" role="img" aria-label="Consultant portrait, selected"></span></li>
    <li>Dolor sit amet<span class="rail photo" role="img" aria-label="Consultant portrait"></span></li>
    <li>Consectetuer<span class="rail photo" role="img" aria-label="Consultant portrait"></span></li>
    <li>Adipiscing<span class="rail photo" role="img" aria-label="Consultant portrait"></span></li>
    <li>Nonummy<span class="rail photo" role="img" aria-label="Consultant portrait"></span></li>
    <li>Euismod<span class="rail photo" role="img" aria-label="Consultant portrait"></span></li>
    <li>Tincidunt<span class="rail photo" role="img" aria-label="Consultant portrait"></span></li>
  </ul>
  <div class="btn yellow full">Back</div>
</section>

<section class="screen c4 r4">
  <header class="appbar"><svg><use href="#i-back"/></svg>Send Message</header>
  <p class="hint" style="margin:0">Please write the text for the SMS and confirm that you want to send it.</p>
  <div class="message-area"></div>
  <div class="btn yellow half-l">Cancel</div>
  <div class="btn blue half-r">Send</div>
</section>

<section class="screen dark c5 r4">
  <div class="sent-avatar" role="img" aria-label="Portrait of the selected consultant"></div>
  <p class="sent-text" style="margin:0">Lorem Ipsum has now<br>received your SMS</p>
  <div class="btn yellow sent-ok">OK</div>
</section>

<section class="screen off c6 r4"></section>
</body>
</html>
```